Employee Benefits and Insurance Consulting

We are an existing company with over 30 years experience but are changing our name. We would like a simple design with grey tones.

Industry/Entity Type

Insurance

Contact Information for Business Card

Marlow Benefits Consulting
Gerald P Odell CEO
5172 Brackenfield Road
Harlan Springs, TN 37940
gerald@marlowbx.com
865-412-3396 - O
865-247-5081 - C

```html
<!DOCTYPE html>
<html lang="en">
<head>
<meta charset="utf-8">
<title>Marlow Benefits Consulting – Business Card</title>
<link rel="stylesheet" href="https://fonts.googleapis.com/css2?family=Questrial&display=swap">
<style>
  :root {
    --page: #e6e4e0;
    --card: #f3f4f4;
    --band-light: #cfd0d2;
    --band-mid: #b7b9bc;
    --band-dark: #9fa2a6;
    --ink: #4a4a4c;
    --ink-soft: #6e6f72;
    --rule: #8d8f92;
  }
  * { margin: 0; padding: 0; box-sizing: border-box; }
  html, body {
    width: 1200px; height: 900px; overflow: hidden;
    background: var(--page);
    font-family: "Questrial", "Century Gothic", sans-serif;
    color: var(--ink);
  }
  .card {
    position: absolute; left: 75px; top: 150px;
    width: 1050px; height: 600px;
    background: var(--card);
    box-shadow: 0 14px 34px rgba(0,0,0,0.18);
    overflow: hidden;
  }
  .card-bands { position: absolute; inset: 0; }
  .divider {
    position: absolute; left: 640px; top: 70px;
    width: 1.5px; height: 455px; background: var(--rule);
  }
  .brand {
    position: absolute; left: 60px; top: 215px; width: 520px;
    display: flex; align-items: center; gap: 22px;
  }
  .brand-dot {
    flex: none; width: 46px; height: 46px; border-radius: 50%;
    background: var(--ink-soft);
  }
  .brand-name {
    font-size: 40px; font-weight: 400; line-height: 1.15; color: var(--ink);
    letter-spacing: 0.5px;
  }
  .contact { position: absolute; left: 690px; top: 120px; width: 340px; }
  .contact-name {
    font-size: 38px; font-weight: 400; line-height: 1.2;
    color: var(--ink); letter-spacing: 0.5px; white-space: nowrap;
  }
  .contact-title {
    font-size: 19px; font-style: italic; color: var(--ink-soft);
    margin: 2px 0 0 118px;
  }
  .contact-lines { list-style: none; margin-top: 48px; }
  .contact-lines li {
    display: flex; align-items: center; gap: 14px;
    font-size: 21px; color: var(--ink-soft); margin-bottom: 10px;
    white-space: nowrap;
  }
  .contact-lines svg { width: 22px; height: 22px; flex: none; }
  .address {
    margin-top: 40px; font-size: 21px; line-height: 1.6;
    color: var(--ink-soft); font-style: normal; white-space: nowrap;
  }
</style>
</head>
<body>
  <section class="card" aria-label="Business card">
    <svg class="card-bands" viewBox="0 0 1050 600" aria-hidden="true">
      <rect x="0" y="0" width="1050" height="38" fill="var(--band-light)"/>
      <polygon points="170,0 560,0 540,38 190,38" fill="var(--band-mid)"/>
      <polygon points="860,0 1050,0 1050,38 880,38" fill="var(--band-dark)"/>
      <polygon points="0,0 40,0 0,38" fill="var(--band-dark)"/>
      <rect x="0" y="545" width="1050" height="55" fill="var(--band-light)"/>
      <polygon points="0,545 170,545 150,600 0,600" fill="var(--band-dark)"/>
      <polygon points="440,545 800,545 820,600 420,600" fill="var(--band-mid)"/>
      <polygon points="990,545 1050,545 1050,600 1010,600" fill="var(--band-dark)"/>
    </svg>

    <div class="brand">
      <span class="brand-dot"></span>
      <span class="brand-name">Marlow Benefits Consulting</span>
    </div>

    <div class="divider"></div>

    <div class="contact">
      <h1 class="contact-name">Gerald P Odell</h1>
      <p class="contact-title">(CEO)</p>
      <ul class="contact-lines">
        <li>
          <svg viewBox="0 0 24 24"><rect x="6" y="2" width="12" height="20" rx="2.5" fill="var(--ink)"/><rect x="8" y="5" width="8" height="12" fill="var(--card)"/><circle cx="12" cy="19.3" r="1" fill="var(--card)"/></svg>
          865-247-5081
        </li>
        <li>
          <svg viewBox="0 0 24 24"><circle cx="12" cy="12" r="11" fill="var(--ink)"/><path d="M8.2 6.5l2 2.2-1 1.6c.8 1.7 2 2.9 3.6 3.7l1.6-1 2.2 2-1.2 1.8c-4.2-.4-8-4.2-8.4-8.4z" fill="var(--card)"/></svg>
          865-412-3396
        </li>
        <li>
          <svg viewBox="0 0 24 24"><rect x="2" y="5" width="20" height="14" rx="1.5" fill="var(--ink)"/><path d="M3 6.5l9 6.5 9-6.5" fill="none" stroke="var(--card)" stroke-width="1.6"/></svg>
          gerald@marlowbx.com
        </li>
      </ul>
      <address class="address">
        5172 Brackenfield Road<br>
        Harlan Springs, TN 37940
      </address>
    </div>
  </section>
</body>
</html>
```